[WEB DESIGN - Start-up] Online LOANS against Luxury Assets - Needs a Web Design

Hello,
We need a web design for a new company. We make online LOANS against Luxury assets.
The name is private, that's why you could remplace it by the term "LOGO" or "ENTERPRISE".

In attachments, you'll find few models that we would like. Nonetheless, we don't want a copy of these screenshots. They are only prototypes that we made. Here we expect you to lead a professional web Design with your intuition and your ideas.

The final design should communicate start-up spirit, professionalism and fluidity.

Best Regards.

Industry/Entity Type

Finance

Number of Pages Required

2 page

Font styles to use
Sans Serif

Colors
f78f20
ffffff
b2b2b2
e9e9e9

Requirements
Must have
• The designer will draw on the 2015 web trends.
• The subject site is serious (loans against luxury assets), but the site should be modern and pleasant.
• PLEASE REFER YOU TO MY MODEL ( ATTACHMENTS)
Nice to have
• Surprise-me ! Welcome to a lot of imagination.

```html
<!DOCTYPE html>
<html lang="en">
<head>
<meta charset="utf-8">
<title>Enterprise – Loans against luxury assets</title>
<link href="https://fonts.googleapis.com/css2?family=Open+Sans:wght@300;400;600;700;800&display=swap" rel="stylesheet">
<style>
:root{
  --orange:#f78f20;
  --white:#ffffff;
  --grey:#b2b2b2;
  --light:#e9e9e9;
  --text:#6d6d6d;
  --dark:#3a3a3a;
  --darker:#2b2b2b;
  --ink:#333333;
}
*{box-sizing:border-box;margin:0;padding:0}
html,body{width:1200px;height:2348px;overflow:hidden}
body{font-family:"Open Sans",Arial,sans-serif;color:var(--text);background:var(--white);position:relative}
section,header,footer{position:absolute;left:0;width:1200px}
p{font-size:13px;line-height:1.55}

/* Hero */
.hero{top:0;height:472px;color:var(--white)}
.hero-photo{position:absolute;inset:0;background:linear-gradient(180deg,#5b4a3c 0%,#7a6553 45%,#4a3b30 100%)}
.hero-shade{position:absolute;inset:0;background:rgba(20,15,10,.45)}
.topbar{position:absolute;top:0;left:0;width:1200px;height:66px;display:flex;align-items:center;justify-content:space-between;padding:0 60px}
.brand{font-weight:800;font-size:28px;letter-spacing:1px;color:var(--white)}
.nav{display:flex;gap:26px;font-size:11px;font-weight:600;letter-spacing:.5px}
.nav a{color:var(--white);text-decoration:none}
.nav a.active{color:var(--orange)}
.hero-title{position:absolute;top:112px;width:100%;text-align:center}
.hero-title .small{font-weight:300;font-size:30px;letter-spacing:2px;line-height:1}
.hero-title .big{font-weight:800;font-size:40px;letter-spacing:1px;line-height:1.2}
.search-form{position:absolute;top:210px;left:280px;width:640px}
.field{height:34px;background:rgba(40,30,22,.6);border:1px solid rgba(255,255,255,.25);display:flex;align-items:center;gap:10px;padding:0 12px;font-size:12px}
.field .dot{width:12px;height:12px;border-radius:50%;background:var(--orange)}
.row{display:flex;gap:20px;margin-bottom:16px}
.row .field{flex:1}
.row .field.half{flex:0 0 310px}
.search-btn{display:block;width:640px;height:34px;margin-top:60px;background:var(--orange);color:var(--white);border:none;font:700 13px "Open Sans",sans-serif;letter-spacing:2px}
.dots{position:absolute;top:326px;left:0;width:100%;display:flex;justify-content:center;gap:8px}
.dots span{width:9px;height:9px;border-radius:50%;background:rgba(255,255,255,.5)}
.dots span.on{background:var(--white)}
.arrow{position:absolute;top:246px}

/* Steps */
.steps{top:472px;height:328px;display:flex}
.step{flex:1;padding:36px 28px 0 38px}
.step:nth-child(odd){background:var(--light)}
.step:nth-child(even){background:var(--white)}
.step-icon{width:38px;height:38px;border:2px solid var(--orange);display:flex;align-items:center;justify-content:center;color:var(--orange);font-weight:700;font-size:13px}
.step h3{color:var(--orange);font-size:17px;font-weight:700;margin:22px 0 12px;letter-spacing:.5px}
.step p{width:190px}

/* Goods */
.goods{top:800px;height:360px;text-align:center}
.goods-photo{position:absolute;inset:0;background:linear-gradient(180deg,#6b5d4f 0%,#4e4237 60%,#3a3029 100%)}
.goods-title{position:absolute;top:110px;width:100%}
.goods-title .kicker{color:var(--orange);font-size:30px;font-weight:700;letter-spacing:1px}
.goods-title .main{color:var(--white);font-size:46px;font-weight:800;letter-spacing:1px;line-height:1.1}

/* Help */
.help{top:1160px;height:360px;text-align:center}
.help h2{margin-top:44px;font-size:24px;font-weight:400;color:var(--ink)}
.help h2 b{color:var(--orange);font-weight:800}
.help-cols{display:flex;justify-content:space-between;width:860px;margin:50px auto 0}
.help-col{width:240px;font-size:14px;color:var(--ink);line-height:1.5}
.help-col .icon{height:90px;display:flex;align-items:flex-end;justify-content:center;margin-bottom:16px}
.help-col b{font-weight:700}
.help-col .phone{font-size:18px;font-weight:600}

/* Company */
.company{top:1520px;height:520px;background:var(--light)}
.company h2{text-align:center;margin-top:52px;font-size:23px;font-weight:400;color:var(--ink)}
.company h2 b{font-weight:800}
.company-cols{display:flex;gap:60px;margin:40px 0 0 80px}
.col{width:490px}
.col-title{display:flex;align-items:center;gap:12px;color:var(--orange);font-weight:800;font-size:16px;letter-spacing:.5px;margin-bottom:18px}
.bubble{background:var(--orange);color:var(--white);padding:14px 18px;font-size:13px;border-radius:4px;width:420px}
.quote{display:flex;align-items:center;gap:18px;margin:14px 0 22px}
.quote.right{flex-direction:row-reverse;justify-content:flex-start;margin-left:30px}
.avatar{width:58px;height:58px;border-radius:50%;background:#c8b5a2;flex:none}
.counters{display:flex;flex-direction:column;gap:18px;margin-top:18px}
.counter{display:flex;align-items:center;gap:18px}
.digits{display:flex;gap:4px}
.digits span{width:30px;height:44px;background:var(--dark);color:var(--white);font-size:24px;font-weight:700;display:flex;align-items:center;justify-content:center}
.counter p{width:230px}

/* Footer */
.footer{top:2040px;height:308px;background:var(--dark);color:#cfcfcf}
.footer-cols{display:flex;padding:38px 80px 0}
.footer h4{color:var(--orange);font-size:16px;font-weight:800;letter-spacing:.5px;margin-bottom:16px}
.footer .about{width:440px}
.footer .about p{margin-bottom:14px}
.footer .links{width:260px;margin-left:60px;padding-top:0;list-style:none;font-size:12px;line-height:1.6;text-transform:uppercase}
.footer .links li.gap{margin-top:10px}
.footer .contact{width:280px}
.footer .contact h4{color:var(--white)}
.copyright{position:absolute;bottom:0;left:0;width:100%;height:34px;background:var(--darker);text-align:center;font-size:11px;line-height:34px;color:#9a9a9a}
</style>
</head>
<body>

<header class="hero">
  <div class="hero-photo" role="img" aria-label="Photograph of luxury watches and jewellery on a display table, warm brown tones"></div>
  <div class="hero-shade"></div>
  <div class="topbar">
    <div class="brand">ENTERPRISE</div>
    <nav class="nav">
      <a class="active">CONCEPT</a><a>PROPERTY</a><a>ESTIMATION</a><a>FAQ</a><a>MY ACCOUNT</a>
    </nav>
  </div>
  <svg class="arrow" style="left:88px" width="16" height="28" viewBox="0 0 16 28"><path d="M14 2 2 14l12 12" fill="none" stroke="#fff" stroke-width="2.5"/></svg>
  <svg class="arrow" style="left:1096px" width="16" height="28" viewBox="0 0 16 28"><path d="M2 2l12 12L2 26" fill="none" stroke="#fff" stroke-width="2.5"/></svg>
  <div class="hero-title">
    <div class="small">ONE TIRES OF</div>
    <div class="big">EVERYTHING EXCEPT MONEY</div>
  </div>
  <form class="search-form">
    <div class="row">
      <div class="field"><span class="dot"></span>Select</div>
      <div class="field"><span class="dot"></span>Redemption Date wishes</div>
    </div>
    <div class="row">
      <div class="field half"><span class="dot"></span>Desired Price</div>
    </div>
    <button class="search-btn" type="button">SEARCH</button>
  </form>
  <div class="dots" style="top:340px"><span class="on"></span><span></span><span></span><span></span><span></span></div>
</header>

<section class="steps">
  <div class="step"><div class="step-icon">01</div><h3>ESTIMATE</h3><p>Lorem Ipsum is simply dummy text of the printing and typesetting industry. Lorem Ipsum has been the standard text since 1500s.</p></div>
  <div class="step"><div class="step-icon">02</div><h3>PAYMENT</h3><p>Lorem Ipsum is simply dummy text of the printing and typesetting industry. Lorem Ipsum has been the standard text since 1500s.</p></div>
  <div class="step"><div class="step-icon">03</div><h3>RECURSATION</h3><p>Lorem Ipsum is simply dummy text of the printing and typesetting industry. Lorem Ipsum has been the standard text since 1500s.</p></div>
  <div class="step"><div class="step-icon">04</div><h3>REDEMPTION</h3><p>Lorem Ipsum is simply dummy text of the printing and typesetting industry. Lorem Ipsum has been the standard text since 1500s.</p></div>
</section>

<section class="goods">
  <div class="goods-photo" role="img" aria-label="Collage of luxury goods categories: jewellery, watches, art, wine and vehicles, dark brown tones"></div>
  <div class="goods-title">
    <div class="kicker">THE GOODS</div>
    <div class="main">WE ACCEPT</div>
  </div>
</section>

<section class="help">
  <h2>NEED HELP! <b>LISTEN TO</b> WE ARE YOUR</h2>
  <div class="help-cols">
    <div class="help-col">
      <div class="icon"><svg width="66" height="60" viewBox="0 0 66 60"><path d="M6 18c0-8 10-12 27-12s27 4 27 12v6H46v-6H20v6H6z" fill="#8a8a8a"/><rect x="12" y="28" width="42" height="28" rx="4" fill="#8a8a8a"/><circle cx="33" cy="42" r="8" fill="#fff"/></svg></div>
      The lanudi to <b>Friday 9am to 19h</b><br><span class="phone">01 23 45 67 89</span>
    </div>
    <div class="help-col">
      <div class="icon"><svg width="70" height="86" viewBox="0 0 70 86" role="img" aria-label="Advisor figure icon"><circle cx="35" cy="22" r="18" fill="#f78f20"/><path d="M4 86c0-22 14-36 31-36s31 14 31 36z" fill="#f78f20"/></svg></div>
      Questions <b>Frequently</b>
    </div>
    <div class="help-col">
      <div class="icon"><svg width="66" height="46" viewBox="0 0 66 46"><rect x="2" y="2" width="62" height="42" fill="#8a8a8a"/><path d="M2 2l31 24L64 2" fill="none" stroke="#fff" stroke-width="3"/></svg></div>
      <b>CONTACT FORM</b><br><b>OR</b><br>contact@pledgora-example.com
    </div>
  </div>
</section>

<section class="company">
  <h2>N1 COMPANY IS THE SALE OF <b>FACULTY WITH AT RACH</b></h2>
  <div class="company-cols">
    <div class="col">
      <div class="col-title"><svg width="22" height="22" viewBox="0 0 22 22"><path d="M2 4h18v11H9l-5 4v-4H2z" fill="#f78f20"/></svg>ORDINERS TESTIMONIALS</div>
      <div class="bubble">Lorem Ipsum is simply dummy text of the printing and typesetting industry.</div>
      <div class="quote">
        <div class="avatar" role="img" aria-label="Customer portrait photo"></div>
        <p>Lorem Ipsum is simply dummy text of the printing and typesetting industry.</p>
      </div>
      <div class="bubble" style="margin-left:30px">Lorem Ipsum is simply dummy text of the printing and typesetting industry.</div>
      <div class="quote right">
        <div class="avatar" role="img" aria-label="Customer portrait photo"></div>
        <p>Lorem Ipsum is simply dummy text of the printing and typesetting industry.</p>
      </div>
    </div>
    <div class="col">
      <div class="col-title"><svg width="22" height="22" viewBox="0 0 22 22"><rect x="2" y="12" width="4" height="8" fill="#f78f20"/><rect x="9" y="7" width="4" height="13" fill="#f78f20"/><rect x="16" y="2" width="4" height="18" fill="#f78f20"/></svg>SOME NUMBERS</div>
      <p>Lorem Ipsum is simply dummy text of the printing and typesetting industry. Lorem Ipsum has been the industry's standard dummy text ever since the 1500s, when an unknown printer took a galley of type and scrambled it to make a type specimen book. It has survived not only five centuries, but also the leap into electronic typesetting, remaining essentially unchanged.</p>
      <div class="counters">
        <div class="counter"><div class="digits"><span>0</span><span>5</span><span>3</span><span>2</span><span>3</span></div><p>Lorem Ipsum is simply dummy text of the printing and typesetting industry.</p></div>
        <div class="counter"><div class="digits"><span>0</span><span>4</span><span>5</span><span>6</span><span>8</span></div><p>Lorem Ipsum is simply dummy text of the printing and typesetting industry.</p></div>
      </div>
    </div>
  </div>
</section>

<footer class="footer">
  <div class="footer-cols">
    <div class="about">
      <h4>SALE TO REPURCHASE</h4>
      <p>Lorem Ipsum is simply dummy text of the printing and typesetting industry. Lorem Ipsum has been the industry's standard dummy text ever since the 1500s, when an unknown printer took a galley of type and scrambled it.</p>
      <p>Lorem Ipsum is simply dummy text of the printing and typesetting industry.</p>
    </div>
    <ul class="links">
      <li>Home</li><li>Concept</li><li>The estimates</li><li>FAQ</li><li>Who are we?</li>
      <li class="gap">My account</li><li>Sell property</li><li>Buy a property</li>
    </ul>
    <div class="contact">
      <h4>CONTACT US</h4>
      <p>SAS Pledgora<br>12 Rue des Lilas<br>75011 Paris</p>
      <p style="margin-top:10px">Registered company with capital of 10 000 euros. Siret 000 000 000 00000.</p>
    </div>
  </div>
  <div class="copyright">© 2015 ENTERPRISE. All Rights Reserved</div>
</footer>

</body>
</html>
```